DESIGN specific documents

We need precise design of certain documents and certain, for our law firm. Specifically we seek: 1) Design a format for report or legal report (legal opinion) 2) Design of a format fee proposal (proposal fee) 3) Design template PPT 4) Website design Designs must take our corporate logo and a simulated document structure proposals must come the word format in addition to the classic vector file formats

Target Market(s)

Business

Industry/Entity Type

Legal

Number of Pages Required

3 page

Requirements
Must have
• Corporate Logo Design Report attached should consider a cover and report sheets
Nice to have
• simulate a design on recycled paper

```html
<!DOCTYPE html>
<html lang="en">
<head>
<meta charset="utf-8">
<title>Velarde &amp; Asociados – Document Set</title>
<link rel="stylesheet" href="https://fonts.googleapis.com/css2?family=Tinos:ital,wght@0,400;0,700;1,400;1,700&family=Open+Sans:ital,wght@0,400;0,600;0,700;1,300;1,400&display=swap">
<style>
:root{
  --brand-blue:#0e5a7e;
  --brand-blue-dark:#0a4662;
  --slate:#5f7d8c;
  --cream:#fbf8d8;
  --band-grey:#f1f2f3;
  --cell-grey:#eceef0;
  --ink:#444;
  --ink-soft:#666;
  --stage:#2b2b2b;
  --white:#fff;
}
*{box-sizing:border-box;margin:0;padding:0}
html,body{width:1200px;height:1200px;overflow:hidden;background:var(--stage)}
.canvas{position:relative;width:1200px;height:1200px}
.sheet{position:absolute;overflow:hidden;background:var(--white)}
.abs{position:absolute}

/* brand lockup */
.brand{position:absolute;display:flex;flex-direction:column;align-items:center;text-align:center;font-family:"Tinos",serif;color:var(--brand-blue)}
.brand-mark{width:14px;height:14px;background:var(--brand-blue);margin-bottom:8px}
.brand-name{font-size:15px;letter-spacing:.3px;white-space:nowrap}
.brand-sub{font-size:8px;letter-spacing:4px;margin-top:3px;white-space:nowrap}

/* fee proposal */
.fee{left:45px;top:46px;width:525px;height:680px;font-family:"Tinos",serif}
.fee .brand{left:0;top:30px;width:205px}
.fee .title-bar{left:357px;top:22px;width:168px;height:32px;background:var(--brand-blue);color:var(--white);font-style:italic;font-size:24px;line-height:32px;padding-left:20px}
.fee .date{left:370px;top:71px;font-style:italic;font-size:12px;color:var(--ink)}
.fee .date-line{left:370px;top:90px;font-size:12px;color:var(--ink);letter-spacing:.5px}
.band{left:0;width:525px;background:var(--band-grey)}
.section-label{left:0;width:102px;height:40px;background:var(--brand-blue);color:var(--white);font-weight:700;font-style:italic;font-size:11.5px;line-height:13px;padding:6px 0 0 8px;text-transform:uppercase}
.section-label.single{font-size:9.5px;padding-top:14px}
.field{left:115px;width:395px;display:flex;font-style:italic;font-size:8.5px;color:var(--ink-soft);gap:8px}
.field span{display:flex;flex:1;white-space:nowrap}
.field span::after{content:"";flex:1;border-bottom:1px dotted #888;margin:0 0 2px 3px}
.consult-text{left:113px;top:424px;width:400px;font-style:italic;font-size:8.6px;line-height:13.6px;color:var(--ink)}
.schedule{left:195px;top:519px;width:318px;border-collapse:separate;border-spacing:2px}
.schedule td{background:var(--cell-grey);height:17px;text-align:center;font-style:italic;font-size:8.5px;color:var(--ink-soft);width:50%}
.schedule-note{left:10px;top:562px;width:160px;font-style:italic;font-size:5.5px;line-height:11px;color:var(--ink-soft)}
.sign{top:640px;font-style:italic;font-size:11.5px;color:var(--ink)}
.fee-foot{left:0;top:666px;height:14px}

/* report cover */
.report{left:600px;top:44px;width:522px;height:676px;background:var(--brand-blue);font-family:"Open Sans",sans-serif}
.photo{position:absolute}
.report .strip-photo{left:0;top:0;width:44px;height:312px;background:linear-gradient(180deg,#8fa8c2,#5d7d9c 60%,#a7b9c9)}
.report .cream{left:44px;top:0;width:156px;height:676px;background:var(--cream)}
.report .tower-photo{left:200px;top:0;width:322px;height:308px;background:linear-gradient(160deg,#d9e6f3 0%,#a9c3de 35%,#3d6a92 60%,#8aa3bb 85%,#6a8f5a 100%)}
.report .circle-photo{left:10px;top:212px;width:228px;height:228px;border-radius:50%;border:3px solid var(--white);background:radial-gradient(circle at 40% 60%,#e8d2c2 0%,#c9b2a0 25%,#4a4a4a 55%,#1f1f1f 100%)}
.report .brand{left:44px;top:36px;width:156px}
.report .brand-name{font-size:11.5px;letter-spacing:.2px}
.report .brand-sub{font-size:6px;letter-spacing:3px}
.report-title{left:240px;top:410px;color:var(--white);font-style:italic;font-weight:300;font-size:21px;line-height:32px}
.report-foot{left:200px;top:612px;width:322px;text-align:center;color:var(--white)}
.report-foot .firm{font-weight:700;font-size:12px;letter-spacing:.3px}
.report-foot .lines{font-size:8.6px;line-height:14px;margin-top:4px}

/* welcome slide */
.slide{left:304px;top:754px;width:560px;height:418px;background:var(--brand-blue);font-family:"Open Sans",sans-serif}
.slide .facade-photo{left:0;top:17px;width:560px;height:236px;background:linear-gradient(165deg,#f2f2f2 0%,#c8ccd0 35%,#8e959c 60%,#b6bcc2 80%,#d9dcde 100%)}
.slide .brand{left:12px;top:84px;width:265px}
.slide .brand-name{font-size:19px}
.slide .brand-sub{font-size:9px;letter-spacing:7px}
.slide .brand-mark{width:18px;height:18px;margin-bottom:12px}
.slide .tab{left:164px;top:241px;width:225px;height:14px;background:var(--brand-blue-dark)}
.welcome{right:32px;top:276px;color:var(--white);font-weight:700;font-size:38px;letter-spacing:.5px}
.welcome-sub{right:32px;top:322px;color:var(--white);font-size:19px}
.contacts{left:19px;top:374px;display:flex;gap:10px;color:var(--white);font-size:8.8px;line-height:13px}
.contacts div div{display:flex;align-items:center;gap:3px;white-space:nowrap}
.contacts svg{width:9px;height:9px;fill:var(--white)}
</style>
</head>
<body>
<main class="canvas">

  <section class="sheet fee" aria-label="Fee proposal form">
    <div class="brand">
      <div class="brand-mark"></div>
      <div class="brand-name">VELARDE &amp; ASOCIADOS</div>
      <div class="brand-sub">ABOGADOS</div>
    </div>
    <div class="abs title-bar">Fee Proposal</div>
    <div class="abs date">Date: (DD/MM/YYYY)</div>
    <div class="abs date-line">............/............. /...............</div>

    <div class="abs band" style="top:223px;height:81px"></div>
    <div class="abs band" style="top:411px;height:80px"></div>

    <div class="abs section-label" style="top:152px">Client<br>Information</div>
    <div class="abs field" style="top:137px"><span>Last Name :</span><span>First Name :</span></div>
    <div class="abs field" style="top:159px"><span>Company Name :</span></div>
    <div class="abs field" style="top:181px"><span>Contact No :</span><span>Email :</span></div>
    <div class="abs field" style="top:204px"><span>Website Address :</span></div>

    <div class="abs section-label" style="top:242px">Proposal<br>Information</div>
    <div class="abs field" style="top:232px"><span>Project Name :</span></div>
    <div class="abs field" style="top:258px"><span>Reference Number:</span><span>Revision Number :</span></div>
    <div class="abs field" style="top:283px"><span>Data Submitted :</span></div>

    <div class="abs section-label" style="top:350px">Project<br>Details</div>
    <div class="abs field" style="top:331px"><span>Lorem Ipsum :</span></div>
    <div class="abs field" style="top:349px"><span>Lorem Ipsum :</span></div>
    <div class="abs field" style="top:368px"><span>Lorem Ipsum :</span></div>
    <div class="abs field" style="top:387px"><span>Lorem Ipsum :</span></div>

    <div class="abs section-label single" style="top:434px">Consultatants</div>
    <p class="abs consult-text">Lorem ipsum dolor sit amet, consectetur adipiscing elit. Sed at ante. Mauris eleifend, quam a vulptate dictum, massa quam dapibus leo, eget vulputate orci purus ut lorem. In fringilla mi in ligula. Pellen tesque aliquam quam vel dolor. Nunc adipiscing. Sed quamodio, tempus ac, aliquam molestie varius ac, tellus. Vestibulum ut nulla aliquam risus rutrum interdum. Pellentesque lorem.</p>

    <div class="abs section-label" style="top:513px">Project<br>Schedule</div>
    <p class="abs schedule-note">Lorem ipsum dolor sit amet, consectetur adipiscing elit. Sed at ante. Mauris eleifend, quam a vulptate dictum, massa quam dapibus leo, eget vulputate orci purus ut lorem. In</p>
    <table class="abs schedule">
      <tr><td>Work Stage</td><td>Duration</td></tr>
      <tr><td>Lorem Ipsum</td><td>Lorem Ipsum</td></tr>
      <tr><td>Lorem Ipsum</td><td>Lorem Ipsum</td></tr>
      <tr><td>Lorem Ipsum</td><td>Lorem Ipsum</td></tr>
      <tr><td>Lorem Ipsum</td><td>Lorem Ipsum</td></tr>
    </table>

    <div class="abs sign" style="left:19px">Signature: .......................................</div>
    <div class="abs sign" style="left:288px">Archiect / Client initials ............. /.............</div>

    <div class="abs fee-foot" style="width:254px;background:var(--slate)"></div>
    <div class="abs fee-foot" style="left:254px;width:271px;background:var(--brand-blue)"></div>
  </section>

  <section class="sheet report" aria-label="Annual legal report cover">
    <div class="photo strip-photo" role="img" aria-label="Photo of a glass office facade"></div>
    <div class="photo cream"></div>
    <div class="photo tower-photo" role="img" aria-label="Photo of a glass office tower against a blue sky"></div>
    <div class="photo circle-photo" role="img" aria-label="Photo of a hand signing a document with a pen"></div>
    <div class="brand">
      <div class="brand-mark"></div>
      <div class="brand-name">VELARDE &amp; ASOCIADOS</div>
      <div class="brand-sub">ABOGADOS</div>
    </div>
    <h1 class="abs report-title">2016 - 2017 ANNUAL<br>COMPANY LEGAL REPORT</h1>
    <div class="abs report-foot">
      <div class="firm">VELARDE &amp; ASOCIADOS. ABOGADOS</div>
      <div class="lines">56 2 3000 1100 • 56 2 3000 1102 | info@velarde-legal.cl | www.velarde-legal.cl<br>Av. Costanera 1200, Of. 804, Providencia, Santiago, PO BOX : CP 7500000</div>
    </div>
  </section>

  <section class="sheet slide" aria-label="Presentation title slide">
    <div class="photo facade-photo" role="img" aria-label="Photo of a glass office building seen from below under a cloudy sky"></div>
    <svg class="abs" style="left:0;top:0" width="560" height="418" viewBox="0 0 560 418">
      <polygon points="120,17 148,17 134,47" fill="var(--brand-blue)"/>
      <polyline points="0,263 74,263 74,300" fill="none" stroke="#3aa0d0" stroke-width="1"/>
      <line x1="163" y1="265" x2="560" y2="265" stroke="#3aa0d0" stroke-width="1"/>
      <circle cx="146" cy="263" r="6.5" fill="var(--brand-blue)" stroke="#5cc3ee" stroke-width="1.5"/>
    </svg>
    <div class="abs tab"></div>
    <div class="brand">
      <div class="brand-mark"></div>
      <div class="brand-name">VELARDE &amp; ASOCIADOS</div>
      <div class="brand-sub">ABOGADOS</div>
    </div>
    <h2 class="abs welcome">WELCOME</h2>
    <div class="abs welcome-sub">TO OUR PRESENTATION</div>
    <div class="abs contacts">
      <div>
        <div><svg viewBox="0 0 10 10"><path d="M1 3c0-1 1-2 4-2s4 1 4 2v1H7V3H3v1H1zM2 5h6l1 4H1z"/></svg>56 2 3000 1100</div>
        <div><svg viewBox="0 0 10 10"><path d="M1 3c0-1 1-2 4-2s4 1 4 2v1H7V3H3v1H1zM2 5h6l1 4H1z"/></svg>56 2 3000 1102</div>
      </div>
      <div>
        <div><svg viewBox="0 0 10 10"><circle cx="5" cy="5" r="4" fill="none" stroke="#fff" stroke-width="1"/><path d="M1 5h8M5 1v8" stroke="#fff" stroke-width=".8"/></svg>www.velarde-legal.cl</div>
        <div><svg viewBox="0 0 10 10"><rect x="1" y="2" width="8" height="6"/></svg>info@velarde-legal.cl</div>
      </div>
      <div>
        <div><svg viewBox="0 0 10 10"><path d="M5 1l4 4H8v4H6V7H4v2H2V5H1z"/></svg>Av. Costanera 1200, Of. 804</div>
        <div style="padding-left:12px">Providencia, Santiago, PO BOX : CP 7500000</div>
      </div>
    </div>
  </section>

</main>
</body>
</html>
```